Mexican construction company needs a business card design

We need a business card design for a company based in Monterrey, Mexico called:

Desarrollos Quilbeta S.A. de C.V.

The company is in the construction business and I would like the businees card to be simple and concise. Please use white background and blue or black text color that say:

"Proyectos de Construcción"-- (Brief description of business)
" Rodrigo Velun Osorio"--- (My name)
"rvelun@correoplat.mx"-- (My email)
"C: (81) 52 19 67 43"-- (My cell)
"O: (81) 56 72 18 94"-- (Office phone)

Please use only the colors of my company that are attached

Please make the back of the business card blue (same blue from logo) and use the logo.

Thanks!

```html
<!DOCTYPE html>
<html lang="es">
<head>
<meta charset="utf-8">
<title>Desarrollos Quilbeta – Tarjeta de presentación</title>
<link href="https://fonts.googleapis.com/css2?family=Lato:wght@400;700&display=swap" rel="stylesheet">
<style>
  :root {
    --navy: #02023d;
    --steel: #9a9a9c;
    --ink-soft: #8a8a8e;
    --white: #ffffff;
    --backdrop: #e9e7e4;
  }
  * { box-sizing: border-box; margin: 0; padding: 0; }
  html, body {
    width: 1200px; height: 1000px; overflow: hidden;
    background: var(--backdrop);
    font-family: "Lato", Arial, sans-serif;
  }
  .canvas { position: relative; width: 1200px; height: 1000px; }
  .card {
    position: absolute; left: 265px; width: 666px; height: 397px;
    box-shadow: 0 3px 10px rgba(0,0,0,0.18);
  }
  .card--front { top: 73px; background: var(--navy); }
  .card--back { top: 533px; background: var(--white); }

  .brand { position: absolute; display: flex; align-items: center; gap: 18px; }
  .brand__square { display: block; background: var(--steel); }
  .brand__name { font-weight: 700; text-transform: uppercase; line-height: 1.05; letter-spacing: 0.04em; }
  .brand__line { display: block; }

  .card--front .brand { left: 130px; top: 137px; }
  .card--front .brand__square { width: 110px; height: 110px; }
  .card--front .brand__name { color: var(--white); }
  .card--front .brand__line--small { font-size: 28px; }
  .card--front .brand__line--large { font-size: 40px; }

  .card--back .brand { left: 33px; top: 149px; gap: 14px; }
  .card--back .brand__square { width: 86px; height: 86px; }
  .card--back .brand__name { color: var(--navy); }
  .card--back .brand__line--small { font-size: 20px; }
  .card--back .brand__line--large { font-size: 29px; }

  .divider {
    position: absolute; left: 375px; top: 127px; width: 2px; height: 140px;
    background: linear-gradient(to bottom, rgba(2,2,61,0), var(--navy) 30%, var(--navy) 70%, rgba(2,2,61,0));
  }
  .contact { position: absolute; left: 407px; top: 140px; }
  .contact__name { font-size: 20px; font-weight: 700; color: var(--navy); margin-bottom: 17px; }
  .contact__list { list-style: none; }
  .contact__item {
    display: flex; align-items: center; gap: 8px;
    font-size: 16px; color: var(--ink-soft); height: 25.5px;
  }
  .contact__icon { width: 14px; height: 14px; fill: var(--navy); flex: none; }
</style>
</head>
<body>
<main class="canvas">
  <section class="card card--front" aria-label="Reverso de la tarjeta">
    <div class="brand">
      <span class="brand__square" aria-hidden="true"></span>
      <p class="brand__name">
        <span class="brand__line brand__line--small">Desarrollos</span>
        <span class="brand__line brand__line--large">Quilbeta</span>
      </p>
    </div>
  </section>

  <section class="card card--back" aria-label="Frente de la tarjeta">
    <div class="brand">
      <span class="brand__square" aria-hidden="true"></span>
      <p class="brand__name">
        <span class="brand__line brand__line--small">Desarrollos</span>
        <span class="brand__line brand__line--large">Quilbeta</span>
      </p>
    </div>
    <div class="divider" aria-hidden="true"></div>
    <div class="contact">
      <h1 class="contact__name">Rodrigo Velun Osorio</h1>
      <ul class="contact__list">
        <li class="contact__item">
          <svg class="contact__icon" viewBox="0 0 14 14" aria-hidden="true"><path d="M4 0h6a1 1 0 0 1 1 1v12a1 1 0 0 1-1 1H4a1 1 0 0 1-1-1V1a1 1 0 0 1 1-1zm0.5 1.5v9.5h5V1.5zM7 11.6a0.7 0.7 0 1 0 0 1.4a0.7 0.7 0 0 0 0-1.4z"/></svg>
          (81) 52 19 67 43
        </li>
        <li class="contact__item">
          <svg class="contact__icon" viewBox="0 0 14 14" aria-hidden="true"><path d="M1 5c0-2 3-3 6-3s6 1 6 3v1.2h-3V4.8H4v1.4H1zM3.5 7h7l2 3.5V13h-11v-2.5zM7 8.3a1.6 1.6 0 1 0 0 3.2a1.6 1.6 0 0 0 0-3.2z"/></svg>
          (81) 56 72 18 94
        </li>
        <li class="contact__item">
          <svg class="contact__icon" viewBox="0 0 14 14" aria-hidden="true"><path d="M0 3h14v1L7 8.5L0 4zM0 5.3l7 4.5l7-4.5V11H0z"/></svg>
          rvelun@correoplat.mx
        </li>
      </ul>
    </div>
  </section>
</main>
</body>
</html>
```